Velmar Industrial Coatings

We are looking to improve our business cards. Our company installs industrial floor and wall coatings in industrial, chemical and food processing plants.
Our coatings which consist of epoxy, urethane, and vinyl esters provide chemical and abrasion resistant surface with non-skid properties that are easy to clean.

Target Market(s)

food manufacturing, chemical plants, breweries and wineries, warehouses, clean room floors.

Industry/Entity Type

Construction

Contact Information for Business Card

improved current logo.

Colors

Designer to choose colors to be used in the design.

Requirements
Must have
• the information from uploaded file
Nice to have
• "We'll be outstanding on your floors."

```html
<!DOCTYPE html>
<html lang="en">
<head>
<meta charset="utf-8">
<title>Velmar Industrial Coatings – Business Cards</title>
<link rel="stylesheet" href="https://fonts.googleapis.com/css2?family=Open+Sans:wght@400;600&family=Tinos&display=swap">
<style>
  :root {
    --bg: #e9e9eb;
    --card-dark: #141416;
    --card-light: #f4f4f6;
    --brand-blue: #4650b4;
    --text-dark: #1e1e22;
    --text-grey: #5a5a60;
    --text-light: #e8e8ec;
    --accent-red: #8a2b2b;
  }
  * { box-sizing: border-box; margin: 0; padding: 0; }
  html, body {
    width: 1200px; height: 825px; overflow: hidden;
    background: var(--bg);
    font-family: "Open Sans", Arial, sans-serif;
  }
  .stage {
    width: 1200px; height: 825px;
    display: flex; align-items: center; justify-content: center; gap: 40px;
  }
  .card {
    position: relative;
    width: 540px; height: 310px;
    box-shadow: 0 6px 18px rgba(0,0,0,.18);
    overflow: hidden;
  }

  /* Front */
  .card-front { background: var(--card-dark); }
  .card-front .wordmark {
    position: absolute; left: 120px; top: 92px;
    display: flex; align-items: center; gap: 16px;
    color: var(--text-light);
  }
  .wordmark .mark-square {
    width: 58px; height: 58px; background: var(--brand-blue);
  }
  .wordmark .name {
    font-weight: 400; line-height: 1.1;
  }
  .wordmark .name-main { display: block; font-size: 42px; letter-spacing: 3px; }
  .wordmark .name-sub { display: block; font-size: 12.5px; letter-spacing: 2.6px; text-transform: uppercase; }
  .card-front .site {
    position: absolute; left: 70px; bottom: 56px;
    font-size: 11px; letter-spacing: 1.6px; color: var(--brand-blue);
  }

  /* Back */
  .card-back { background: var(--card-light); color: var(--text-dark); }
  .contact-name {
    position: absolute; left: 44px; top: 62px;
    font-size: 19px; font-weight: 400;
  }
  .contact-tollfree {
    position: absolute; left: 44px; top: 89px;
    font-family: "Tinos", "Times New Roman", serif;
    font-size: 11px; color: var(--accent-red);
  }
  .divider {
    position: absolute; left: 40px; right: 40px; top: 110px;
    height: 1px; background: var(--brand-blue);
  }
  .phone-list {
    position: absolute; left: 44px; top: 124px;
    list-style: none; font-size: 12px; color: var(--text-grey);
  }
  .phone-list li { display: flex; align-items: center; gap: 8px; height: 20px; }
  .phone-list svg { width: 11px; height: 11px; fill: var(--brand-blue); }
  .card-back .wordmark {
    position: absolute; right: 42px; top: 40px;
    display: flex; align-items: center; gap: 10px;
    color: var(--text-dark);
  }
  .card-back .wordmark .mark-square { width: 38px; height: 38px; }
  .card-back .wordmark .name-main { font-size: 27px; letter-spacing: 2px; }
  .card-back .wordmark .name-sub { font-size: 8px; letter-spacing: 1.6px; }
  .address {
    position: absolute; right: 42px; top: 190px;
    display: flex; align-items: flex-start; gap: 10px;
    font-size: 13px; color: var(--text-grey); text-align: right; line-height: 1.5;
  }
  .address svg { width: 11px; height: 15px; fill: var(--brand-blue); margin-top: 22px; }
  .footer-band {
    position: absolute; left: 0; right: 0; bottom: 0; height: 38px;
    background: var(--brand-blue);
    display: flex; align-items: center; padding-left: 130px;
    color: #fff; font-size: 13px; letter-spacing: 2.4px;
  }
</style>
</head>
<body>
<main class="stage">
  <section class="card card-front" aria-label="Business card front">
    <div class="wordmark">
      <span class="mark-square"></span>
      <span class="name"><span class="name-main">VELMAR</span><span class="name-sub">Industrial Coatings Inc.</span></span>
    </div>
    <p class="site">www.velmarfloors.com</p>
  </section>

  <section class="card card-back" aria-label="Business card back">
    <h1 class="contact-name">Mara Quill</h1>
    <p class="contact-tollfree">1-800-555-0142</p>
    <div class="divider"></div>
    <ul class="phone-list">
      <li><svg viewBox="0 0 12 12"><path d="M1 4c0-2 2-3 5-3s5 1 5 3l-2 1-1-1V3H4v1L3 5zM2 6h8v5H2zm3 1v3h2V7z"/></svg>(360) 555-0131</li>
      <li><svg viewBox="0 0 12 12"><path d="M3 1h6v3H3zM1 5h10v5H9v1H3v-1H1zm3 3v2h4V8z"/></svg>(360) 555-0133</li>
      <li><svg viewBox="0 0 12 12"><path d="M3 0h6v12H3zm1 1v8h4V1zm2 9a.6.6 0 100 1.2A.6.6 0 006 10z"/></svg>(360) 555-0177</li>
    </ul>
    <div class="wordmark">
      <span class="mark-square"></span>
      <span class="name"><span class="name-main">VELMAR</span><span class="name-sub">Industrial Coatings Inc.</span></span>
    </div>
    <address class="address" style="font-style:normal">
      <span>Velmar Inc.<br>PO Box 42<br>Harlow, WA 98500</span>
      <svg viewBox="0 0 12 16"><path d="M6 0a6 6 0 00-6 6c0 4 6 10 6 10s6-6 6-10a6 6 0 00-6-6zm0 8.5A2.5 2.5 0 116 3.5a2.5 2.5 0 010 5z"/></svg>
    </address>
    <div class="footer-band">www.velmarfloors.com</div>
  </section>
</main>
</body>
</html>
```